pharmacy/travel clinic business card design

We need a business card for our new business called Brenwick Travel Clinic and Pharmacy. Our primary focus is doing consultations for people before travelling internationally and providing vaccinations and prescriptions for them. While the business is considered a pharmacy, it has more the look and feel of a doctor's office. The design should communicate a professional and trustworthy feel. I have attached a copy of the logo we are going to be using.
Updates
Thanks for the submissions.  If you haven`t been eliminated you are one of the finalists.  Decision will likely be made tomorrow.

Target Market(s)
Customers, other health care professionals, travel agents
Industry/Entity Type
Clinic
Look and feel
Each slider illustrates characteristics of the customer's brand and the style your logo design should communicate.

```html
<!DOCTYPE html>
<html lang="en">
<head>
<meta charset="utf-8">
<title>Brenwick Travel Clinic and Pharmacy – Business Card</title>
<link href="https://fonts.googleapis.com/css2?family=Ubuntu:wght@500;700&family=Arimo:wght@400&display=swap" rel="stylesheet">
<style>
  :root {
    --navy: #2b3f9f;
    --royal: #2f5fc4;
    --sky: #29a8e3;
    --lime: #8cc63f;
    --paper: #ffffff;
    --backdrop: #5a5a5a;
    --ink-light: #ffffff;
  }
  * { box-sizing: border-box; margin: 0; padding: 0; }
  html, body {
    width: 1067px; height: 1200px; overflow: hidden;
    background: var(--backdrop);
  }
  .sheet {
    position: relative; width: 1067px; height: 1200px;
    display: flex; flex-direction: column; align-items: center;
    justify-content: center; gap: 80px;
  }
  .card {
    position: relative; width: 700px; height: 400px; overflow: hidden;
    box-shadow: 0 14px 30px rgba(0,0,0,0.45);
  }
  .brand-name {
    font-family: "Ubuntu", sans-serif; font-weight: 700;
    color: var(--lime); line-height: 0.98; letter-spacing: -0.5px;
  }
  .brand-name span { display: block; }
  .brand-mark-dot {
    border-radius: 50%; background: var(--sky); flex: none;
  }

  /* Front */
  .card--front {
    background: linear-gradient(100deg, var(--navy) 0%, var(--royal) 50%, var(--sky) 100%);
  }
  .card--front .brand {
    position: absolute; left: 44px; top: 140px;
    display: flex; align-items: flex-start; gap: 14px;
  }
  .card--front .brand-mark-dot { width: 34px; height: 34px; margin-top: 12px; }
  .card--front .brand-name { font-size: 56px; }
  .card--front .brand-name .brand-sub { font-size: 26px; margin-top: 6px; }

  /* Back */
  .card--back { background: var(--paper); }
  .card--back .brand {
    position: absolute; left: 36px; top: 40px;
    display: flex; align-items: flex-start; gap: 10px;
  }
  .card--back .brand-mark-dot { width: 24px; height: 24px; margin-top: 8px; }
  .card--back .brand-name { font-size: 40px; }
  .card--back .brand-name .brand-sub { font-size: 19px; margin-top: 4px; }
  .accent-band {
    position: absolute; left: 0; right: 0; top: 186px; height: 16px;
    background: var(--lime);
  }
  .info-panel {
    position: absolute; left: 0; right: 0; top: 212px; bottom: 0;
    background: linear-gradient(100deg, var(--sky) 0%, var(--royal) 55%, var(--navy) 100%);
    color: var(--ink-light); font-family: "Arimo", sans-serif;
    display: flex; justify-content: space-between;
    padding: 34px 40px 0 44px;
  }
  .person-name { font-size: 27px; }
  .person-title { font-size: 16px; margin-top: 2px; }
  .person-address { font-size: 17px; line-height: 1.35; margin-top: 22px; }
  .contact-list { list-style: none; font-size: 17px; line-height: 1.55; margin-top: -2px; }
  .contact-label { color: var(--lime); display: inline-block; width: 16px; }
</style>
</head>
<body>
<main class="sheet">
  <section class="card card--front" aria-label="Business card front">
    <div class="brand">
      <div class="brand-mark-dot"></div>
      <p class="brand-name"><span>Brenwick</span><span>Travel Clinic</span><span class="brand-sub">and PHARMACY</span></p>
    </div>
  </section>

  <section class="card card--back" aria-label="Business card back">
    <div class="brand">
      <div class="brand-mark-dot"></div>
      <p class="brand-name"><span>Brenwick</span><span>Travel Clinic</span><span class="brand-sub">and PHARMACY</span></p>
    </div>
    <div class="accent-band"></div>
    <div class="info-panel">
      <div class="person">
        <p class="person-name">Daniel Mercer</p>
        <p class="person-title">President/CEO</p>
        <p class="person-address">1420 E. Halden Ave. Ste. 210,<br>Larkspur, AZ 85700</p>
      </div>
      <ul class="contact-list">
        <li><span class="contact-label">p.</span> 520 555 0148</li>
        <li><span class="contact-label">t.</span> 866 555 0192</li>
        <li><span class="contact-label">e.</span> daniel@brenwickclinic.com</li>
        <li><span class="contact-label">w.</span> www.brenwickclinic.com</li>
      </ul>
    </div>
  </section>
</main>
</body>
</html>
```